Stylish Business Card for Modern hair salon

I need a simple business card design using our salon logo and colours that are in the logo. We service clients of all ages but predominantly those in the 18 to 55 age range. We have a young staff and are looking to have a card that will present a modern and clean image that represents who we are. The card should be in black and white same as our logo. Minimal use of other colours is allowed.

Industry/Entity Type

Hair And Beauty

Contact Information for Business Card

The design should have the following information
salon name - TR Hair Studio
address - 2751 Birchfield Rd.E. Mississauga, ON L7P3K2
phone - 905 614-2870
website - trhairexample.ca
instagram - tr.hairstudio
twitter - @TR_HairStudio

Colors
000000
ffffff
474747

Requirements
Must have
• simple design, salon name, address, phone, website, instagram, twitter info
• Back of card should have the following:
• YOUR NEXT APPOINTMENT
• DATE
• TIME
Nice to have
• simple design, clear to see and read,
• predominantly black and white colour, minimal use of other colours is ok
Should not have
• many colours, various fonts

```html
<!DOCTYPE html>
<html lang="en">
<head>
<meta charset="utf-8">
<title>TR Hair Studio – Business Card</title>
<link rel="stylesheet" href="https://fonts.googleapis.com/css2?family=Open+Sans:wght@400;600;700&display=swap">
<style>
  :root {
    --backdrop: #d9d7d4;
    --card: #000000;
    --card-edge: #1c1c1c;
    --ink: #ffffff;
    --ink-soft: #c9c9c9;
    --ink-muted: #474747;
    --rule: #9a9a9a;
  }
  * { box-sizing: border-box; margin: 0; padding: 0; }
  html, body {
    width: 1200px; height: 864px; overflow: hidden;
    background: var(--backdrop);
    font-family: "Open Sans", Arial, sans-serif;
  }
  .canvas { position: relative; width: 1200px; height: 864px; }
  .card {
    position: absolute;
    width: 560px; height: 320px;
    background: var(--card);
    border: 1px solid var(--card-edge);
    color: var(--ink);
    box-shadow: 0 10px 30px rgba(0,0,0,.25);
  }
  .card--back { left: 60px; top: 70px; }
  .card--front { left: 580px; top: 450px; }

  /* Back side: appointment card */
  .back-brand {
    position: absolute; left: 40px; top: 92px;
    font-size: 30px; font-weight: 600; letter-spacing: 1px;
    color: var(--ink-muted); line-height: 1.15;
  }
  .appointment { position: absolute; left: 260px; top: 96px; width: 260px; }
  .appointment__title { font-size: 17px; font-weight: 700; color: var(--ink-soft); margin-bottom: 22px; }
  .appointment__row {
    display: flex; align-items: flex-end; gap: 6px;
    font-size: 14px; color: var(--ink-soft); margin-bottom: 22px;
  }
  .appointment__blank { flex: 1; border-bottom: 1px dotted var(--ink-soft); height: 14px; }
  .appointment__suffix { font-size: 10px; }

  /* Front side: contact card */
  .front-brand {
    position: absolute; right: 44px; top: 62px; text-align: right;
    font-size: 40px; font-weight: 600; letter-spacing: 1px; line-height: 1.1;
  }
  .front-rule { position: absolute; left: 36px; right: 36px; top: 176px; height: 1px; background: var(--rule); }
  .person { position: absolute; left: 36px; top: 44px; }
  .person__name { font-size: 14px; font-weight: 700; letter-spacing: .5px; }
  .person__role { font-size: 14px; margin-bottom: 14px; }
  .contact { list-style: none; font-size: 13px; line-height: 1.55; }
  .contact li { display: flex; align-items: center; gap: 8px; }
  .contact__mark { width: 11px; height: 11px; flex: none; }
  .address {
    position: absolute; right: 44px; bottom: 34px; text-align: right;
    font-size: 14px; line-height: 1.45;
  }
  .address__web { letter-spacing: 1.5px; }
</style>
</head>
<body>
<main class="canvas">

  <section class="card card--back" aria-label="Card back: appointment reminder">
    <div class="back-brand">TR Hair<br>Studio</div>
    <div class="appointment">
      <p class="appointment__title">Your Next Appointment</p>
      <p class="appointment__row"><span>Date:</span><span class="appointment__blank"></span></p>
      <p class="appointment__row"><span>Time:</span><span class="appointment__blank"></span><span class="appointment__suffix">AM/PM</span></p>
    </div>
  </section>

  <section class="card card--front" aria-label="Card front: contact details">
    <div class="person">
      <p class="person__name">ALEX MORGAN</p>
      <p class="person__role">CEO/FOUNDER</p>
      <ul class="contact">
        <li>
          <svg class="contact__mark" viewBox="0 0 12 12" aria-hidden="true"><path fill="#fff" d="M2.5 1h2l1 3-1.3 1a7 7 0 0 0 2.8 2.8l1-1.3 3 1v2c0 .8-.7 1.5-1.5 1.5A9.5 9.5 0 0 1 1 2.5C1 1.7 1.7 1 2.5 1z"/></svg>
          905 614-2870
        </li>
        <li>
          <svg class="contact__mark" viewBox="0 0 12 12" aria-hidden="true"><rect x="1" y="1" width="10" height="10" fill="#fff"/></svg>
          @TR_HairStudio
        </li>
        <li>
          <svg class="contact__mark" viewBox="0 0 12 12" aria-hidden="true"><rect x="1" y="1" width="10" height="10" fill="#fff"/></svg>
          tr.hairstudio
        </li>
      </ul>
    </div>

    <div class="front-brand">TR Hair<br>Studio</div>
    <div class="front-rule"></div>

    <address class="address" style="font-style:normal">
      2751 Birchfield Rd.E.<br>
      Mississauga, ON L7P3K2<br>
      <span class="address__web">www.trhairexample.ca</span>
    </address>
  </section>

</main>
</body>
</html>
```